Business Card Design Project

We need a business card design for an existing company in Dallas/Fort Worth that is expanding services and re-branding. We are changing the name from Bristow Commercial Cleaning to Kelmont Facility Services. We are expanding from only commercial cleaning to include complete commercial landscape and facility maintenance services, too.

As stated, we offer a package of services that includes landscape, janitorial and facility services, which is largely unique in the industry.

We would like a design that communicates trust/partnership with a professional, corporate image, but not necessarily using the standard white business card. We would like a design that perhaps uses darker blues or perhaps a gray background, but we are open to other ideas. We might also be interested in a double-sided design - maybe with our logo on the back, printed on a gray background?

We will probably stick with the attached logo, but if you've got another inspired idea....

Target Market(s)

Property managers, commercial real estate professionals, corporate executives

Industry/Entity Type

Landscape

Requirements
Should not have
• Not interested in old style fonts.

```html
<!DOCTYPE html>
<html lang="en">
<head>
<meta charset="utf-8">
<title>Kelmont Facility Services – Business Card</title>
<link href="https://fonts.googleapis.com/css2?family=Mulish:wght@400;700&display=swap" rel="stylesheet">
<style>
  :root {
    --page-bg: #d9d6d2;
    --ink: #1b1b1b;
    --ink-soft: #2a2a2a;
    --paper-light: #ffffff;
    --paper-mid: #c9c9c9;
    --night-top: #0e0e0e;
    --night-bottom: #a9a9a9;
    --on-dark: #f2f2f2;
    --silver-1: #f5f5f5;
    --silver-2: #8a8a8a;
    --silver-3: #3a3a3a;
  }
  * { box-sizing: border-box; margin: 0; padding: 0; }
  html, body { width: 1200px; height: 900px; overflow: hidden; }
  body {
    background: var(--page-bg);
    display: flex;
    flex-direction: column;
    align-items: center;
    justify-content: center;
    gap: 30px;
    font-family: "Mulish", sans-serif;
  }
  .card {
    position: relative;
    width: 700px;
    height: 400px;
    overflow: hidden;
    box-shadow: 0 10px 24px rgba(0,0,0,.28);
  }
  .card--front {
    background: linear-gradient(160deg, var(--paper-light) 0%, #ececec 45%, var(--paper-mid) 100%);
    color: var(--ink);
  }
  .card--back {
    background: linear-gradient(160deg, var(--night-top) 0%, #3a3a3a 45%, var(--night-bottom) 100%);
    color: var(--on-dark);
  }
  .silver-band {
    position: absolute;
    left: 0; right: 0; bottom: 0;
    height: 22px;
    background: linear-gradient(90deg, var(--silver-1) 0%, var(--silver-2) 25%, var(--silver-3) 45%, var(--silver-1) 70%, var(--silver-2) 100%);
    border-top: 1px solid rgba(255,255,255,.7);
  }
  .brand {
    position: absolute;
    top: 34px;
    left: 34px;
  }
  .brand__line {
    display: flex;
    align-items: center;
    gap: 12px;
  }
  .brand__dot {
    width: 22px;
    height: 22px;
    border-radius: 50%;
    background: currentColor;
    flex: none;
  }
  .brand__name {
    font-size: 32px;
    font-weight: 400;
    line-height: 1.1;
  }
  .brand__tagline {
    font-size: 13px;
    margin-top: 6px;
    margin-left: 34px;
  }
  .person {
    position: absolute;
    top: 120px;
    left: 56px;
  }
  .person__marker {
    position: absolute;
    left: -26px;
    top: 5px;
    width: 0; height: 0;
    border-top: 11px solid transparent;
    border-bottom: 11px solid transparent;
    border-left: 16px solid var(--ink);
  }
  .person__name { font-size: 27px; font-weight: 700; }
  .person__title { font-size: 17px; font-weight: 700; color: var(--ink-soft); margin-top: 2px; }
  .contact {
    position: absolute;
    top: 214px;
    left: 34px;
    list-style: none;
    font-size: 18px;
  }
  .contact__row {
    display: flex;
    align-items: center;
    gap: 12px;
    height: 32px;
  }
  .contact__icon { width: 24px; height: 24px; flex: none; }
  .contact__fax { display: inline-flex; align-items: center; gap: 10px; margin-left: 22px; }
  .web-address {
    position: absolute;
    left: 60px;
    bottom: 70px;
    font-size: 30px;
    letter-spacing: 1px;
    color: var(--on-dark);
  }
</style>
</head>
<body>

<section class="card card--front" aria-label="Business card front">
  <div class="brand">
    <div class="brand__line">
      <div class="brand__dot"></div>
      <div class="brand__name">Kelmont Facility Services</div>
    </div>
    <div class="brand__tagline">Grounds, cleaning and building care from a single partner</div>
  </div>

  <div class="person">
    <div class="person__marker"></div>
    <div class="person__name">Marcus Hale</div>
    <div class="person__title">General Manager</div>
  </div>

  <ul class="contact">
    <li class="contact__row">
      <svg class="contact__icon" viewBox="0 0 24 24" aria-hidden="true"><rect width="24" height="24" rx="5" fill="#1b1b1b"/><path d="M5 12 L12 6 L19 12 H17 V18 H7 V12 Z" fill="#fff"/></svg>
      123 main st 00000 xxxxx 321 321
    </li>
    <li class="contact__row">
      <svg class="contact__icon" viewBox="0 0 24 24" aria-hidden="true"><rect width="24" height="24" rx="5" fill="#1b1b1b"/><path d="M8 5 C6 7 6 11 9 15 C12 19 15 19 17 18 L15 15 L13 16 C11 15 9 12 9 10 L11 9 Z" fill="#fff"/></svg>
      (000) 000-0000
      <span class="contact__fax">
        <svg class="contact__icon" viewBox="0 0 24 24" aria-hidden="true"><rect width="24" height="24" rx="5" fill="#1b1b1b"/><rect x="8" y="4" width="8" height="5" fill="#fff"/><rect x="5" y="10" width="14" height="7" fill="#fff"/><rect x="8" y="15" width="8" height="5" fill="#fff" stroke="#1b1b1b" stroke-width="1"/></svg>
        (000) 000-0000
      </span>
    </li>
    <li class="contact__row">
      <svg class="contact__icon" viewBox="0 0 24 24" aria-hidden="true"><rect width="24" height="24" rx="5" fill="#1b1b1b"/><text x="12" y="17" text-anchor="middle" font-family="Mulish, sans-serif" font-weight="700" font-size="14" fill="#fff">@</text></svg>
      info@kelmontfacilityservices.com
    </li>
    <li class="contact__row">
      <svg class="contact__icon" viewBox="0 0 24 24" aria-hidden="true"><rect width="24" height="24" rx="5" fill="#1b1b1b"/><g fill="none" stroke="#fff" stroke-width="1.5"><circle cx="12" cy="12" r="6.5"/><ellipse cx="12" cy="12" rx="3" ry="6.5"/><line x1="5.5" y1="12" x2="18.5" y2="12"/></g></svg>
      www.kelmontfacilityservices.com
    </li>
  </ul>

  <div class="silver-band"></div>
</section>

<section class="card card--back" aria-label="Business card back">
  <div class="brand">
    <div class="brand__line">
      <div class="brand__dot"></div>
      <div class="brand__name">Kelmont Facility Services</div>
    </div>
    <div class="brand__tagline">Grounds, cleaning and building care from a single partner</div>
  </div>
  <div class="web-address">www.kelmontfacilityservices.com</div>
  <div class="silver-band"></div>
</section>

</body>
</html>
```